Brightmoor Partners Branding Revamp

We are a consulting company, looking for a way to display and promote our brand. We have 2 sides to the business- Brightmoor (financial) and Partners (cyber security). The financial side products relate to business necessities: card processing, website design/hosting/maintenance, VoIP phone systems. The cyber security side promotes a bundled package of 4 solutions: network vulnerability scan, dark web scan, anti-ransomeware/malware software, and image-level backups. We want people to understand that partnering with Brightmoor Partners gives them “Elevated Peace of Mind” (tagline). Current badge and logos uploaded.

Target Market(s)

Small businesses

Contact Information for Business Card

Lena Marwick, Vice President, lena@brightmoorpartners.example, 555-806-1937, www.brightmoorpartners.example

Requirements
Nice to have
• I do prefer the darker background for front and back

```html
<!DOCTYPE html>
<html lang="en">
<head>
<meta charset="utf-8">
<title>Brightmoor Partners — Business Card</title>
<link href="https://fonts.googleapis.com/css2?family=Montserrat:wght@300;400;500;700;800&display=swap" rel="stylesheet">
<style>
  :root {
    --backdrop: #e4e4e4;
    --card: #262626;
    --card-pattern-dark: #1d1d1d;
    --card-pattern-light: #2b2b2b;
    --band: #2a2a2a;
    --red: #e0141e;
    --red-deep: #a80d14;
    --white: #ffffff;
  }
  * { box-sizing: border-box; margin: 0; padding: 0; }
  html, body { width: 1200px; height: 1200px; overflow: hidden; }
  body {
    background: var(--backdrop);
    font-family: "Montserrat", sans-serif;
    position: relative;
  }
  .card {
    position: absolute;
    top: 250px;
    width: 420px;
    height: 680px;
    border-radius: 28px;
    background: var(--card);
    overflow: hidden;
    box-shadow: 0 14px 30px rgba(0,0,0,0.25);
  }
  .card--front { left: 150px; }
  .card--back { left: 630px; }

  /* Front */
  .brand {
    position: absolute;
    top: 150px;
    left: 0; right: 0;
    text-align: center;
  }
  .brand__name {
    color: var(--white);
    font-weight: 700;
    font-size: 34px;
    letter-spacing: 9px;
    padding-left: 9px;
    line-height: 1;
  }
  .brand__sub {
    margin-top: 12px;
    color: var(--red);
    font-weight: 700;
    font-size: 15px;
    letter-spacing: 6px;
    padding-left: 6px;
  }
  .person {
    position: absolute;
    top: 390px;
    left: 0; right: 0;
    text-align: center;
  }
  .person__name {
    color: var(--red);
    font-weight: 800;
    font-size: 30px;
    letter-spacing: 1px;
  }
  .person__title {
    margin-top: 6px;
    color: var(--white);
    font-weight: 400;
    font-size: 20px;
  }
  .contact-icons {
    position: absolute;
    top: 486px;
    left: 40px; right: 40px;
    display: flex;
    align-items: center;
    gap: 12px;
  }
  .contact-icons__rule {
    flex: 1;
    height: 1px;
    background: var(--red-deep);
  }
  .icon {
    width: 30px; height: 30px;
    border-radius: 50%;
    background: radial-gradient(circle at 35% 30%, #ff3a40, var(--red) 55%, var(--red-deep));
    display: flex;
    align-items: center;
    justify-content: center;
  }
  .icon svg { width: 16px; height: 16px; }
  .contact-list {
    position: absolute;
    top: 534px;
    left: 0; right: 0;
    list-style: none;
    text-align: center;
    color: var(--white);
    font-weight: 300;
    font-size: 17px;
    line-height: 1.6;
  }

  /* Back */
  .back-pattern {
    position: absolute;
    inset: 0;
    background: linear-gradient(135deg, var(--card-pattern-light), var(--card-pattern-dark));
  }
  .back-band {
    position: absolute;
    top: 290px;
    left: 0; right: 0;
    height: 100px;
    background: var(--band);
    display: flex;
    align-items: center;
    justify-content: center;
    gap: 16px;
  }
  .back-band__dot {
    width: 14px; height: 14px;
    border-radius: 50%;
    background: var(--red);
  }
  .back-band__text { text-align: left; }
  .back-band__name {
    color: var(--white);
    font-weight: 700;
    font-size: 24px;
    letter-spacing: 6px;
    line-height: 1;
  }
  .back-band__sub {
    margin-top: 6px;
    color: var(--red);
    font-weight: 700;
    font-size: 11px;
    letter-spacing: 4px;
  }
</style>
</head>
<body>

  <section class="card card--front" aria-label="Business card front">
    <div class="brand">
      <div class="brand__name">BRIGHTMOOR</div>
      <div class="brand__sub">PARTNERS</div>
    </div>

    <div class="person">
      <div class="person__name">LENA MARWICK</div>
      <div class="person__title">Vice President</div>
    </div>

    <div class="contact-icons">
      <span class="contact-icons__rule"></span>
      <span class="icon" aria-label="Phone">
        <svg viewBox="0 0 24 24"><path fill="#fff" d="M6.6 10.8a15.1 15.1 0 0 0 6.6 6.6l2.2-2.2c.3-.3.7-.4 1-.2 1.1.4 2.3.6 3.6.6.6 0 1 .4 1 1V20c0 .6-.4 1-1 1A17 17 0 0 1 3 4c0-.6.4-1 1-1h3.5c.6 0 1 .4 1 1 0 1.3.2 2.5.6 3.6.1.3 0 .7-.2 1z"/></svg>
      </span>
      <span class="icon" aria-label="Email">
        <svg viewBox="0 0 24 24"><path fill="#fff" d="M3 6h18v12H3z"/><path fill="none" stroke="#c0101a" stroke-width="1.6" d="M3 6l9 7 9-7"/></svg>
      </span>
      <span class="icon" aria-label="Website">
        <svg viewBox="0 0 24 24"><circle cx="12" cy="12" r="9" fill="none" stroke="#fff" stroke-width="1.8"/><ellipse cx="12" cy="12" rx="4" ry="9" fill="none" stroke="#fff" stroke-width="1.5"/><path d="M3 12h18" stroke="#fff" stroke-width="1.5"/></svg>
      </span>
      <span class="contact-icons__rule"></span>
    </div>

    <ul class="contact-list">
      <li>555-806-1937</li>
      <li>lena@brightmoorpartners.example</li>
      <li>www.brightmoorpartners.example</li>
    </ul>
  </section>

  <section class="card card--back" aria-label="Business card back">
    <div class="back-pattern" role="img" aria-label="Subtle tone-on-tone repeating geometric pattern covering the card back"></div>
    <div class="back-band">
      <span class="back-band__dot"></span>
      <div class="back-band__text">
        <div class="back-band__name">BRIGHTMOOR</div>
        <div class="back-band__sub">PARTNERS</div>
      </div>
    </div>
  </section>

</body>
</html>
```